Lumen Path - Fiber Internet to the home postcard

Design a postcard for my company, Lumen Path, using the logo below. On the front of the card:
- No Buffering • No BS
- Second line should be the logo
- $60 / month • 10-Gigs
- lumenpath.net

Color palate should follow the colors in the logo.

Address should say
- Special pricing during construction
- Our best price
- Our fastest speed
- $60 / month • 10-Gigs
- lumenpath.net

Target Market(s)

25 - 55 year olds. Middle income/class. People with kids and pick up trucks

Industry/Entity Type

Fiber Internet Service Provider

Font styles to use
Sans Serif

Colors

Designer to choose colors to be used in the design.

Requirements
Nice to have
• I am open to more creative changes

```html
<!DOCTYPE html>
<html lang="en">
<head>
<meta charset="utf-8">
<title>Lumen Path Postcard</title>
<link rel="stylesheet" href="https://fonts.googleapis.com/css2?family=Barlow:wght@300;700;800&family=Barlow+Condensed:wght@600;700&display=swap">
<style>
  :root {
    --backdrop: #cfcfcf;
    --green: #62b43a;
    --green-light: #7ec845;
    --green-dark: #3f8f22;
    --navy: #0b2a5e;
    --white: #ffffff;
    --rule: #d9d9d9;
    --stamp: #dcdcdc;
  }
  * { box-sizing: border-box; margin: 0; padding: 0; }
  html, body { width: 960px; height: 1200px; overflow: hidden; }
  body { background: var(--backdrop); position: relative; font-family: "Barlow", Arial, sans-serif; }

  .card {
    position: absolute; left: 69px; width: 806px; height: 538px;
    overflow: hidden; background: var(--white);
    box-shadow: 0 2px 6px rgba(0,0,0,.25);
  }
  .card--front { top: 43px; }
  .card--back { top: 613px; }
  .abs { position: absolute; }

  /* Front */
  .front-field {
    left: 0; top: 0; width: 806px; height: 422px;
    background: radial-gradient(ellipse at 60% 40%, var(--green-light), var(--green) 70%);
  }
  .mascot-area { border-radius: 90px 90px 20px 20px; }
  .front-mascot { left: 34px; top: 37px; width: 160px; height: 353px;
    background: linear-gradient(180deg, var(--navy) 0 38%, #e9f1e4 38% 62%, rgba(11,42,94,.5) 62%); opacity: .85; }
  .front-tagline { left: 209px; top: 18px; color: var(--white); font-weight: 800; font-size: 50px; letter-spacing: -0.5px; white-space: nowrap; }
  .front-brand { left: 218px; top: 95px; color: var(--navy); font-weight: 800; font-size: 104px; line-height: 1; letter-spacing: -3px; white-space: nowrap; }
  .offer-band { left: 120px; top: 267px; width: 686px; height: 68px; background: var(--navy); display: flex; align-items: center; padding-left: 12px; }
  .offer-band__text { color: var(--white); font-weight: 800; font-size: 52px; margin-left: 12px; white-space: nowrap; }
  .dot { color: var(--green); }
  .front-url { left: 280px; top: 344px; color: var(--white); font-weight: 800; font-size: 42px; display: flex; align-items: center; gap: 8px; }
  .front-waves { left: 0; top: 380px; }
  .front-contact { left: 0; top: 422px; width: 806px; height: 116px; }
  .phone-large { left: 98px; top: 455px; color: var(--navy); font-weight: 700; font-size: 54px; white-space: nowrap; }
  .divider { left: 499px; top: 448px; width: 1px; height: 78px; background: var(--rule); }
  .service-area { left: 581px; top: 458px; color: var(--navy); font-weight: 700; font-size: 16.5px; line-height: 19.5px; }

  /* Back */
  .back-field { left: 0; top: 0; width: 445px; height: 538px;
    background: radial-gradient(ellipse at 40% 55%, var(--green-light), var(--green) 75%); }
  .back-mascot { left: 0; top: 185px; width: 210px; height: 295px;
    background: linear-gradient(180deg, var(--navy) 0 40%, #e9f1e4 40% 62%, rgba(11,42,94,.45) 62%); opacity: .85; }
  .back-headline { left: 0; top: 14px; width: 440px; text-align: center; font-weight: 700; font-size: 46px; line-height: 46px; color: var(--white); letter-spacing: -0.5px; }
  .back-headline .accent { color: var(--green); }
  .best-price { left: 208px; top: 184px; width: 202px; display: flex; align-items: center; justify-content: flex-end; gap: 6px;
    font-family: "Barlow Condensed", Arial, sans-serif; font-weight: 700; font-size: 29px; color: var(--white); }
  .speed-badge { left: 223px; top: 224px; width: 194px; height: 194px; border-radius: 50%;
    background: var(--navy); border: 4px solid var(--green-light); text-align: center; color: var(--white); }
  .speed-badge__icon { margin-top: 22px; }
  .speed-badge__label { font-weight: 300; font-size: 17px; margin-top: 2px; }
  .speed-badge__price { font-family: "Barlow Condensed", Arial, sans-serif; font-weight: 600; font-size: 40px; line-height: 40px; }
  .speed-badge__speed { font-family: "Barlow Condensed", Arial, sans-serif; font-weight: 600; font-size: 38px; line-height: 40px; color: var(--green-light); }
  .back-url { left: 190px; top: 428px; width: 225px; display: flex; justify-content: flex-end; align-items: center; gap: 6px;
    color: var(--white); font-weight: 800; font-size: 30px; }
  .back-contact { left: 0; top: 480px; width: 445px; height: 58px; }
  .phone-small { left: 55px; top: 491px; color: var(--white); font-weight: 700; font-size: 29px; white-space: nowrap; }
  .service-area--small { left: 319px; top: 496px; color: var(--white); font-weight: 700; font-size: 8.6px; line-height: 10.5px; }
  .stamp { left: 690px; top: 28px; width: 86px; height: 106px; background: var(--stamp); }
  .address-line { left: 494px; width: 282px; height: 1px; background: var(--rule); }
  .back-brand { left: 500px; top: 436px; color: var(--navy); font-weight: 800; font-size: 58px; letter-spacing: -1.5px; white-space: nowrap; }
</style>
</head>
<body>

<section class="card card--front">
  <div class="abs front-field"></div>
  <div class="abs front-mascot mascot-area" role="img" aria-label="Cartoon mascot waving, standing beside the headline"></div>

  <div class="abs front-tagline">NO BUFFERING • NO BS</div>
  <div class="abs front-brand">Lumen Path</div>

  <div class="abs offer-band">
    <svg width="56" height="40" viewBox="0 0 56 40" aria-hidden="true">
      <path d="M6 36 A22 22 0 0 1 50 36" fill="none" stroke="var(--green)" stroke-width="7" stroke-dasharray="9 3"/>
      <path d="M28 36 L38 6" stroke="var(--green)" stroke-width="4" stroke-linecap="round"/>
      <circle cx="28" cy="34" r="4" fill="var(--green)"/>
    </svg>
    <span class="offer-band__text">$60 / MONTH <span class="dot">•</span> 10-GIGS</span>
  </div>

  <div class="abs front-url">
    <svg width="26" height="26" viewBox="0 0 26 26" aria-hidden="true">
      <circle cx="13" cy="13" r="11" fill="none" stroke="#fff" stroke-width="2.5"/>
      <ellipse cx="13" cy="13" rx="5" ry="11" fill="none" stroke="#fff" stroke-width="2"/>
      <path d="M2 13H24M4 8H22M4 18H22" stroke="#fff" stroke-width="2"/>
    </svg>
    lumenpath.net
  </div>

  <div class="abs front-contact"></div>
  <svg class="abs front-waves" width="806" height="80" viewBox="0 0 806 80" aria-hidden="true">
    <path d="M0 40 C200 -10 420 20 560 36 S760 34 806 26" fill="none" stroke="var(--navy)" stroke-width="2"/>
    <path d="M0 70 C160 10 380 20 520 40 S720 52 806 42" fill="none" stroke="var(--green)" stroke-width="2"/>
    <path d="M0 56 C220 20 420 32 600 48 S760 40 806 30" fill="none" stroke="var(--green-dark)" stroke-width="1.5"/>
  </svg>

  <svg class="abs" style="left:32px;top:458px" width="58" height="58" viewBox="0 0 58 58" aria-hidden="true">
    <circle cx="29" cy="29" r="29" fill="var(--green)"/>
    <path d="M20 15c2-1 4 0 5 2l2 5c1 2 0 3-1 4l-2 2c1 3 4 6 7 7l2-2c1-1 3-2 4-1l5 2c2 1 3 3 2 5l-1 2c-2 3-6 4-10 2-7-3-13-9-16-16-2-4-1-8 2-10z" fill="#fff"/>
    <path d="M33 16a10 10 0 0 1 9 9M33 11a15 15 0 0 1 14 14" fill="none" stroke="#fff" stroke-width="2.5" stroke-linecap="round"/>
  </svg>
  <div class="abs phone-large">(386) 555-0142</div>
  <div class="abs divider"></div>
  <svg class="abs" style="left:510px;top:458px" width="58" height="58" viewBox="0 0 58 58" aria-hidden="true">
    <circle cx="29" cy="29" r="29" fill="var(--green)"/>
    <path d="M29 46c-7-9-12-15-12-21a12 12 0 0 1 24 0c0 6-5 12-12 21z" fill="#fff"/>
    <circle cx="29" cy="25" r="4.5" fill="var(--green)"/>
  </svg>
  <div class="abs service-area">Internet Service Provider<br>to Florida’s Volusia and<br>Brevard Counties</div>
</section>

<section class="card card--back">
  <div class="abs back-field"></div>
  <svg class="abs" style="left:0;top:0" width="520" height="538" viewBox="0 0 520 538" aria-hidden="true">
    <path d="M0 0H440 L444 160 C300 172 150 178 0 174Z" fill="var(--navy)"/>
    <path d="M0 538V480 C150 474 300 474 440 482 L440 538Z" fill="var(--navy)"/>
    <path d="M445 0 C470 120 440 300 455 538" fill="none" stroke="var(--navy)" stroke-width="2"/>
    <path d="M452 0 C480 160 448 340 468 538" fill="none" stroke="var(--green)" stroke-width="2"/>
    <path d="M440 0 C458 180 430 360 450 538" fill="none" stroke="var(--green-light)" stroke-width="1.5"/>
  </svg>
  <div class="abs back-mascot mascot-area" role="img" aria-label="Cartoon mascot with arms out and wifi signals"></div>

  <div class="abs back-headline">SPECIAL<br>PRICING DURING<br><span class="accent">CONSTRUCTION</span></div>

  <div class="abs best-price">
    <svg width="26" height="22" viewBox="0 0 26 22" aria-hidden="true">
      <path d="M12 4h12v14H12z M16 1l4 3" fill="none" stroke="#fff" stroke-width="2"/>
      <path d="M1 10h6l4 3v6H1z" fill="#fff"/>
    </svg>
    OUR BEST PRICE
  </div>

  <div class="abs speed-badge">
    <svg class="speed-badge__icon" width="54" height="34" viewBox="0 0 56 36" aria-hidden="true">
      <path d="M6 34 A22 22 0 0 1 50 34" fill="none" stroke="var(--green)" stroke-width="7" stroke-dasharray="9 3"/>
      <path d="M28 34 L36 4" stroke="var(--green)" stroke-width="4" stroke-linecap="round"/>
      <circle cx="28" cy="32" r="4" fill="var(--green)"/>
    </svg>
    <div class="speed-badge__label">Our fastest speed</div>
    <div class="speed-badge__price">$60 / MONTH</div>
    <div class="speed-badge__speed">10-GIGS</div>
  </div>

  <div class="abs back-url">
    <svg width="20" height="20" viewBox="0 0 26 26" aria-hidden="true">
      <circle cx="13" cy="13" r="11" fill="none" stroke="#fff" stroke-width="2.5"/>
      <ellipse cx="13" cy="13" rx="5" ry="11" fill="none" stroke="#fff" stroke-width="2"/>
      <path d="M2 13H24M4 8H22M4 18H22" stroke="#fff" stroke-width="2"/>
    </svg>
    lumenpath.net
  </div>

  <svg class="abs" style="left:18px;top:493px" width="32" height="32" viewBox="0 0 58 58" aria-hidden="true">
    <circle cx="29" cy="29" r="29" fill="var(--green)"/>
    <path d="M20 15c2-1 4 0 5 2l2 5c1 2 0 3-1 4l-2 2c1 3 4 6 7 7l2-2c1-1 3-2 4-1l5 2c2 1 3 3 2 5l-1 2c-2 3-6 4-10 2-7-3-13-9-16-16-2-4-1-8 2-10z" fill="var(--navy)"/>
  </svg>
  <div class="abs phone-small">(386) 555-0142</div>
  <svg class="abs" style="left:280px;top:493px" width="32" height="32" viewBox="0 0 58 58" aria-hidden="true">
    <circle cx="29" cy="29" r="29" fill="var(--green)"/>
    <path d="M29 46c-7-9-12-15-12-21a12 12 0 0 1 24 0c0 6-5 12-12 21z" fill="var(--navy)"/>
    <circle cx="29" cy="25" r="4.5" fill="var(--green)"/>
  </svg>
  <div class="abs service-area--small">Internet Service Provider<br>to Florida’s Volusia and<br>Brevard Counties</div>

  <div class="abs stamp"></div>
  <div class="abs address-line" style="top:200px"></div>
  <div class="abs address-line" style="top:254px"></div>
  <div class="abs address-line" style="top:307px"></div>
  <div class="abs address-line" style="top:361px"></div>
  <div class="abs back-brand">Lumen Path</div>
</section>

</body>
</html>
```